Celling poster

It is a celling poster with questions that you ask yourself in the morning and a morning prayer + evening questions. People might put it on celling or on the wall.

Here is the contant, it is in Slovenian, but I have send you translation.

PO JUTRU SE DAN POZNA ...

1. Kaj me trenutno najbolj veseli v življenju?
3. Na kaj sem ponosna v življenju?
4. Za katere stvari danes čutim največ hvaležnosti?
5. V čem trenutno najbolj uživam?
6. Koga imam rada in kdo me ima rad?

Danes vstajam
s pomočjo nebeških sil:
svetlobe sonca,
sija lune,
žara ognja,
hitrosti strele,
okretnosti vetra,
globine morja,
stanovitnosti zemlje,
trdnosti skale.

VEČERNE MODROSTI

1. Kaj je bil danes moj prispevek svetu?
2. Kaj sem se danes naučila?
3. Katera situacija v dnevu mi je prinesla največ občutkov topline?

TRANSLATION for your understanding.

MORNING POWER QUESTIONS
1. What am I happy abou in my life right now?
2. What am I excited about in my life now?
3. What am I proud about in my life now?
4. What am I grateful about in my life now?
5. What am I enjoying most in my life now?
6. Who do I love? Who loves me?

MORNING PRAYER
Today I am waking up with the power of heavenly forces.
With the light of sun,
light of moon,
light of fire,
speed of lightning,
flexibility of wind,
depps of ocean,
stability of earth and
hardness of rock.

EVENING QUESTIONS OF WISDOM
1. What have I given today?
2. What did I learn today?
3. Which situations today gave me the most feelings of love, warmth?

```html
<!DOCTYPE html>
<html lang="sl">
<head>
<meta charset="UTF-8">
<title>Po jutru se dan pozna</title>
<link href="https://fonts.googleapis.com/css2?family=Bebas+Neue&family=Barlow+Semi+Condensed:wght@500&family=Lato:wght@400&display=swap" rel="stylesheet">
<style>
  :root {
    --teal: #009483;
    --white: #ffffff;
    --ink: #3a3a3c;
    --night: #2a2a2c;
    --backdrop: #ecebe8;
  }
  * { margin: 0; padding: 0; box-sizing: border-box; }
  html, body {
    width: 1200px; height: 1200px; overflow: hidden;
    background: var(--backdrop);
  }
  .poster {
    position: absolute; left: 204px; top: 30px;
    width: 792px; height: 1140px;
    overflow: hidden;
  }
  .morning {
    position: absolute; left: 0; top: 0; width: 100%; height: 502px;
    background: var(--teal); color: var(--white);
  }
  .morning-title {
    position: absolute; left: 36px; top: 28px;
    font-family: "Bebas Neue", sans-serif; font-weight: 400;
    font-size: 92px; line-height: 1; letter-spacing: 0.5px;
    white-space: nowrap;
  }
  .question-list { list-style: none; }
  .question-list li {
    position: absolute; left: 48px;
    display: flex; align-items: center; gap: 18px;
    font-family: "Barlow Semi Condensed", sans-serif; font-weight: 500;
    font-size: 27px; line-height: 1; white-space: nowrap;
    transform: translateY(-50%);
  }
  .tick { width: 22px; height: 22px; flex: none; }
  .morning .question-list li:nth-child(1) { top: 164px; }
  .morning .question-list li:nth-child(2) { top: 228px; }
  .morning .question-list li:nth-child(3) { top: 292px; }
  .morning .question-list li:nth-child(4) { top: 358px; }
  .morning .question-list li:nth-child(5) { top: 422px; }

  .prayer {
    position: absolute; left: 0; top: 502px; width: 100%; height: 281px;
    background: var(--white); color: var(--ink);
  }
  .section-title {
    position: absolute; left: 0; width: 100%; text-align: center;
    font-family: "Bebas Neue", sans-serif; font-weight: 400;
    font-size: 66px; line-height: 1;
  }
  .prayer .section-title { top: 52px; }
  .accent { color: var(--teal); }
  .prayer-text {
    position: absolute; left: 36px; top: 138px; width: 718px;
    font-family: "Lato", sans-serif; font-size: 24px; line-height: 30px;
    text-align: justify;
  }

  .evening {
    position: absolute; left: 0; top: 783px; width: 100%; height: 357px;
    background: var(--night); color: var(--white);
  }
  .evening-art {
    position: absolute; left: 300px; top: 0; width: 260px; height: 357px;
    background: radial-gradient(ellipse at 50% 45%, rgba(120,120,120,0.35), rgba(42,42,44,0) 70%);
  }
  .evening .section-title { top: 48px; }
  .evening .section-title .light { color: var(--white); }
  .evening .question-list li { font-size: 25px; gap: 20px; }
  .evening .question-list li:nth-child(1) { top: 154px; }
  .evening .question-list li:nth-child(2) { top: 202px; }
  .evening .question-list li:nth-child(3) { top: 251px; }
</style>
</head>
<body>
<svg width="0" height="0" style="position:absolute">
  <defs>
    <symbol id="tick-icon" viewBox="0 0 22 22">
      <circle cx="11" cy="11" r="11" fill="#ffffff"/>
      <path d="M6 11.5 L9.5 15 L16 7.5" fill="none" stroke="currentColor" stroke-width="3" stroke-linecap="round" stroke-linejoin="round"/>
    </symbol>
  </defs>
</svg>

<main class="poster">
  <section class="morning">
    <h1 class="morning-title">PO JUTRU SE DAN POZNA</h1>
    <ul class="question-list">
      <li><svg class="tick" style="color:var(--teal)"><use href="#tick-icon"/></svg>Kaj me trenutno najbolj veseli v življenju?</li>
      <li><svg class="tick" style="color:var(--teal)"><use href="#tick-icon"/></svg>Na kaj sem ponosna v življenju?</li>
      <li><svg class="tick" style="color:var(--teal)"><use href="#tick-icon"/></svg>Za katere stvari danes čutim največ hvaležnosti?</li>
      <li><svg class="tick" style="color:var(--teal)"><use href="#tick-icon"/></svg>V čem trenutno najbolj uživam?</li>
      <li><svg class="tick" style="color:var(--teal)"><use href="#tick-icon"/></svg>Koga imam rada in kdo me ima rad?</li>
    </ul>
  </section>

  <section class="prayer">
    <h2 class="section-title"><span class="accent">DANES</span> VSTAJAM</h2>
    <p class="prayer-text">s pomočjo nebeških sil: svetlobe sonca, sija lune, žara ognja, hitrosti strele, okretnosti vetra, globine morja, stanovitnosti zemlje, trdnosti skale.</p>
  </section>

  <section class="evening">
    <div class="evening-art" role="img" aria-label="Chalk drawing of a head in profile inside a large question mark"></div>
    <h2 class="section-title"><span class="accent">VEČERNE</span> <span class="light">MODROSTI</span></h2>
    <ul class="question-list">
      <li><svg class="tick" style="color:var(--night)"><use href="#tick-icon"/></svg>Kaj je bil danes moj prispevek svetu?</li>
      <li><svg class="tick" style="color:var(--night)"><use href="#tick-icon"/></svg>Kaj sem se danes naučila?</li>
      <li><svg class="tick" style="color:var(--night)"><use href="#tick-icon"/></svg>Katera situacija v dnevu mi je prinesla največ občutkov topline?</li>
    </ul>
  </section>
</main>
</body>
</html>
```